Web design for online activity booking website

Our activity booking website uTrundle.net is looking outdated and needing a loving revamp on its design and STRUCTURE. it was initially created as a destination guide before we modified the homepage slightly to sell activities. So please DON'T RELY on the current website for your design. Now, the focus is ACTIVITY, while guide/ info should come only as secondary.

In other words, we will be doing something very similar to Wandelo.com (a bit crowded for our liking) and FindMyOuting.com. If you could capture the best essences of both, that would be awesome! Besides, we also like roostly.com's simplicity.

SIMPLE, CLEAN, BRIGHT, USER and MOBILE FRIENDLY please :)

We have a new logo created and some wireframes (a few more in progress) so you know the basic components required in each page. These are just rough ideas so please ignore the ratio/size, colours etc and if you have a better way of arranging or simplifying things, please do so :)

Help us make it a website that everyone would love!

Thank you in advance for your time and artistry.

Target Market(s)

Internet savvy travellers between 18-65

Industry/Entity Type

Tourism

Number of Pages Required

5+ page

Requirements
Must have
• SIMPLE, CLEAN feel, USER and MOBILE FRIENDLY please :)
• See attachments for rough structure. Will also need standard pages such as:
• - About Us
• - Contact Us
• - Wishlist etc
• Message from our developer "designer to keep layers in PSD format accurately so html/css code does not need to lead a mess in photoshop"
Nice to have
• UPDATE: We are so thrilled to receive so many web designs but on the other hand, the submissions are getting too generic and everyone's designs is almost looking identical (many look like they are “borrowed” from existing popular websites). This is making the selection and decision process very difficult.
• So instead of sending us more of the very similar homepage design with minor tweaks (which we can do during handover section anyway), please send us a design of more specific page of our website. Please refer job brief, file no. 5 - Product detail page.
• This will give us better idea of your skills and choose the best as winner to work on the rest of our web pages.
Should not have
• No dark background please

```html
<!DOCTYPE html>
<html lang="en">
<head>
<meta charset="utf-8">
<title>uTrundle — Book Activities</title>
<link href="https://fonts.googleapis.com/css2?family=Lato:wght@400;700;900&display=swap" rel="stylesheet">
<style>
:root{
  --blue:#12a3e6;
  --blue-dark:#0b8bd0;
  --green:#3bb54a;
  --pink:#ee2a5c;
  --red-price:#e8204e;
  --orange:#f28a14;
  --ink:#1d1d1d;
  --text:#3a3a3a;
  --muted:#8b8b8b;
  --grey-band:#eef0f3;
  --page:#f4f5f7;
  --white:#ffffff;
  --star:#f2c318;
  --star-off:#d4d4d4;
}
*{box-sizing:border-box;margin:0;padding:0}
html,body{width:1200px;height:1000px;overflow:hidden;background:var(--page);font-family:'Lato',sans-serif;color:var(--text)}
.canvas{position:relative;width:1200px;height:1000px;overflow:hidden;background:#e9eaec}
.screen{position:absolute;top:0;height:1000px;background:var(--white);overflow:hidden}
.screen--desktop{left:0;width:630px;box-shadow:4px 0 10px rgba(0,0,0,.12)}
.screen--compact{left:635px;width:565px}
.abs{position:absolute}

/* hero */
.hero{position:absolute;left:0;top:0;width:100%;background:linear-gradient(180deg,#6f9fb4 0%,#3f8ea0 30%,#2f8a8c 60%,#5b9f93 100%)}
.hero__photo{position:absolute;inset:0;background:radial-gradient(ellipse at 60% 60%,rgba(230,190,170,.45),transparent 45%),radial-gradient(ellipse at 20% 45%,rgba(200,150,120,.35),transparent 30%)}
.logo{position:absolute;display:flex;align-items:center;gap:4px;color:var(--white);font-weight:900}
.logo__dot{width:6px;height:6px;border-radius:50%;background:var(--pink)}
.nav-icons{position:absolute}
.signup{position:absolute;background:var(--blue);color:var(--white);font-weight:700;text-align:center;border-radius:2px}
.hero__title{position:absolute;left:0;width:100%;text-align:center;color:var(--white);font-weight:900;text-shadow:0 2px 6px rgba(0,0,0,.35);line-height:1}
.hero__sub{position:absolute;left:0;width:100%;text-align:center;color:var(--white);font-weight:700;text-shadow:0 2px 5px rgba(0,0,0,.35);line-height:1}
.search{position:absolute;background:rgba(0,0,0,.55);display:flex;align-items:center}
.search__field{background:var(--white);color:var(--ink);display:flex;align-items:center;height:100%}
.search__go{position:absolute;background:var(--blue);color:var(--white);font-weight:900;display:flex;align-items:center;justify-content:center;border-radius:4px}

/* intro */
.intro__kicker{position:absolute;width:100%;text-align:center;color:var(--blue);font-weight:700}
.intro__text{position:absolute;text-align:center;color:var(--ink);line-height:1.35}
.rule{position:absolute;height:1px;background:#c9c9c9}
.section-title{position:absolute;width:100%;text-align:center;color:var(--ink);font-weight:700}

/* destinations */
.tile{position:absolute;display:flex;align-items:center;justify-content:center;color:var(--white);font-weight:700;text-transform:uppercase;text-shadow:0 1px 4px rgba(0,0,0,.6)}
.tile--mono{background:linear-gradient(180deg,#cfcfcf 0%,#8a8a8a 45%,#3c3c3c 100%)}
.tile--night{background:linear-gradient(180deg,#2a2a2a 0%,#9a9a9a 55%,#1c1c1c 100%)}
.tile--sea{background:linear-gradient(180deg,#e5e5e5 0%,#9d9d9d 50%,#5a5a5a 100%)}
.tile--feature{background:linear-gradient(180deg,#d55b8d 0%,#c06db5 35%,#3a3b66 62%,#5d4a67 100%);box-shadow:0 3px 8px rgba(0,0,0,.25)}
.select{position:absolute;background:var(--white);color:var(--muted);display:flex;align-items:center;justify-content:center;border-radius:2px}
.btn-green{position:absolute;background:var(--green);color:var(--white);font-weight:700;display:flex;align-items:center;justify-content:center;border-radius:2px}
.btn-blue{position:absolute;background:var(--blue);color:var(--white);font-weight:700;display:flex;align-items:center;justify-content:center}

/* activities */
.band{position:absolute;left:0;width:100%;background:var(--grey-band)}
.tabs{position:absolute;display:flex;justify-content:space-between;color:var(--muted)}
.tabs .is-active{color:var(--orange)}
.finder{position:absolute;display:flex;align-items:center;gap:4px;color:var(--ink)}
.card{position:absolute;background:var(--white);border-radius:4px;overflow:hidden;box-shadow:0 1px 3px rgba(0,0,0,.1)}
.card--featured{box-shadow:0 4px 12px rgba(0,0,0,.25)}
.card__img{position:relative;width:100%}
.card__img--snorkel{background:linear-gradient(180deg,#2fa7d8 0%,#4bbde0 50%,#2c8fb9 100%)}
.card__img--horse{background:linear-gradient(180deg,#b9d2e0 0%,#e3d8c4 60%,#cdb898 100%)}
.card__img--zip{background:linear-gradient(180deg,#3f7a2e 0%,#6ea13d 55%,#2e5a23 100%)}
.card__img--bike{background:linear-gradient(180deg,#6f8a3f 0%,#a2a865 55%,#857b4e 100%)}
.fav{position:absolute;border-radius:50%;display:flex;align-items:center;justify-content:center}
.fav--pink{background:var(--pink)}
.fav--green{background:var(--green)}
.card__body{color:var(--ink)}
.card__name{font-weight:900;line-height:1.05}
.card__meta{color:var(--muted);font-weight:700;line-height:1.1}
.card__desc{color:var(--muted);line-height:1.2}
.card__row{display:flex;align-items:center;justify-content:space-between}
.price{font-weight:900;color:var(--red-price);line-height:1}
.price--green{color:var(--green)}
.price sup{font-size:.55em;vertical-align:top}
.stars{color:var(--star);letter-spacing:1px}
.stars span{color:var(--star-off)}
.arrow{position:absolute;border:1px solid #333;background:var(--white);display:flex;align-items:center;justify-content:center;color:var(--ink)}

/* islands */
.islands__title{position:absolute;color:var(--ink);font-size:9px;letter-spacing:.5px}
.islands__col{position:absolute;font-size:5.3px;color:var(--text);line-height:11px}
.islands__col h4{color:var(--blue);font-weight:700;font-size:5.3px}
.newsletter{position:absolute;left:0;width:100%;background:var(--orange)}
.newsletter__text{position:absolute;color:var(--white);font-size:5.3px;line-height:1.5}
.newsletter__input{position:absolute;background:var(--white);color:#777;font-size:5px;display:flex;align-items:center;padding-left:7px}
.footer{position:absolute;left:0;width:100%;background:var(--page)}
.footer__col{position:absolute;font-size:5px;line-height:11.5px;color:var(--text)}
.footer__col h5{color:var(--blue);font-size:5.3px;font-weight:400;letter-spacing:.3px}
.social{display:flex;gap:3px;flex-wrap:wrap;width:32px;margin-top:3px}
.social i{width:13px;height:13px;border-radius:50%;background:var(--blue-dark);display:block}
</style>
</head>
<body>
<div class="canvas">

  <!-- ===== Desktop homepage ===== -->
  <section class="screen screen--desktop">
    <header class="hero" style="height:265px">
      <div class="hero__photo" role="img" aria-label="Photo of two smiling kayakers with red paddles on clear turquoise sea"></div>
      <div class="logo" style="left:40px;top:11px;font-size:17px"><span class="logo__dot"></span>uTrundle</div>
      <svg class="nav-icons" style="left:378px;top:11px" width="160" height="16" viewBox="0 0 160 16" fill="none" stroke="#fff" stroke-width="1.6">
        <path d="M8 14 L2 8 A3.5 3.5 0 0 1 8 4 A3.5 3.5 0 0 1 14 8 Z" fill="#fff"/>
        <path d="M30 3h3l2 8h8l2-6H34"/><circle cx="36" cy="14" r="1"/><circle cx="42" cy="14" r="1"/>
        <circle cx="66" cy="8" r="6.5"/><path d="M59.5 8h13M66 1.5c-3 3-3 10 0 13M66 1.5c3 3 3 10 0 13"/>
        <circle cx="97" cy="8" r="6.5"/><path d="M99 5.5c-1-1-4-1-4 .7s4 1 4 2.8-3 1.8-4 .7M97 3.5v9"/>
        <circle cx="128" cy="8" r="6.5" fill="#fff"/><path d="M126 6.5a2 2 0 1 1 2 2v1.5M128 12v.5" stroke="#3f8ea0"/>
        <circle cx="153" cy="5" r="3" fill="#fff"/><path d="M147 15a6 5 0 0 1 12 0Z" fill="#fff"/>
      </svg>
      <div class="signup" style="left:544px;top:10px;width:33px;height:13px;font-size:6.5px;line-height:13px">Sign Up</div>
      <h1 class="hero__title" style="top:116px;font-size:35px;left:-10px">BOOK ACTIVITIES</h1>
      <p class="hero__sub" style="top:152px;font-size:19px;left:-10px">Your Adventure Starts Here!</p>
      <div class="search" style="left:133px;top:207px;width:282px;height:34px;padding:4px 7px;gap:7px">
        <div class="search__field" style="width:132px;font-size:9px;padding-left:5px">Where to, my friend?</div>
        <div class="search__field" style="width:132px;font-size:9px;padding-left:5px">What would you like to do?</div>
      </div>
      <div class="search__go" style="left:417px;top:206px;width:73px;height:37px;font-size:13px">LET'S GO!</div>
    </header>

    <p class="intro__kicker" style="top:280px;font-size:9.5px">Experience the islands with uTrundle</p>
    <p class="intro__text" style="left:95px;top:296px;width:440px;font-size:8.8px">Whether you're looking for sun and sand, a hedonistic weekend or consider yourself to be something of a culture vulture, our aim is to provide all the information you need on our favourite islands.</p>
    <div class="rule" style="left:78px;top:336px;width:459px"></div>

    <h2 class="section-title" style="top:351px;font-size:10px">Explore Our Top Destinations</h2>
    <svg class="abs" style="left:250px;top:366px" width="100" height="16" viewBox="0 0 100 16" fill="none" stroke-width="1.2">
      <rect x="2" y="3" width="12" height="10" rx="1" stroke="#f28a14"/><path d="M4 11l3-4 3 3 2-2 2 3" stroke="#f28a14"/>
      <path d="M93 14s-5-5-5-8a5 5 0 0 1 10 0c0 3-5 8-5 8z" stroke="#444"/><circle cx="93" cy="6" r="1.6" stroke="#444"/>
    </svg>
    <div class="tile tile--mono" style="left:65px;top:390px;width:142px;height:142px;font-size:11px" role="img" aria-label="Black and white photo of a Balearic coastline with agave plants">Balearic</div>
    <div class="tile tile--sea" style="left:230px;top:390px;width:141px;height:142px;font-size:11px" role="img" aria-label="Black and white photo of a Canary Islands beach and mountains">Canary Islands</div>
    <div class="tile tile--night" style="left:395px;top:390px;width:142px;height:142px;font-size:11px" role="img" aria-label="Black and white photo of Ibiza town lit at night">Ibiza</div>
    <div class="tile tile--feature" style="left:65px;top:550px;width:306px;height:142px;font-size:11px;flex-direction:column" role="img" aria-label="Colour photo of a Madeira coastal village at sunset">
      <svg width="18" height="14" viewBox="0 0 18 14" fill="none" stroke="#fff" stroke-width="1.4"><path d="M1 13c1-5 5-8 11-8V1l5 5-5 5V8c-5 0-8 1-11 5z"/></svg>
      <span style="margin-top:6px">Madeira</span>
    </div>
    <div class="select" style="left:116px;top:668px;width:91px;height:18px;font-size:6px">ACTIVITIES&nbsp;&nbsp;&nbsp;&nbsp;&nbsp;&nbsp;&nbsp;▾</div>
    <div class="btn-green" style="left:229px;top:668px;width:90px;height:18px;font-size:6px">BOOK NOW</div>
    <div class="tile tile--sea" style="left:395px;top:550px;width:142px;height:142px;font-size:11px" role="img" aria-label="Black and white photo of a Mallorca harbour">Mallorca</div>
    <div class="btn-blue" style="left:262px;top:702px;width:77px;height:20px;font-size:6.5px">Show more destinations</div>

    <div class="band" style="top:740px;height:260px"></div>
    <h2 class="section-title" style="top:745px;font-size:11px">Explore Our Top Activities</h2>
    <div class="finder" style="left:279px;top:764px;font-size:6.5px">
      <svg width="9" height="9" viewBox="0 0 9 9" fill="none" stroke="#111" stroke-width="1.4"><circle cx="3.6" cy="3.6" r="2.7"/><path d="M5.6 5.6L8.4 8.4"/></svg>Type to search ...
    </div>
    <div class="tabs" style="left:193px;top:779px;width:230px;font-size:6.5px"><span class="is-active">RECOMMENDED</span><span>DESTINATION</span><span>MOST POPULAR</span></div>

    <div class="arrow" style="left:10px;top:881px;width:14px;height:14px;font-size:9px">←</div>
    <div class="arrow" style="left:591px;top:881px;width:14px;height:14px;font-size:9px">→</div>

    <article class="card card--featured" style="left:40px;top:800px;width:128px;height:178px">
      <div class="card__img card__img--snorkel" style="height:86px" role="img" aria-label="Photo of snorkellers swimming in clear blue water">
        <span class="fav fav--green" style="right:12px;bottom:-8px;width:19px;height:19px"><svg width="10" height="9" viewBox="0 0 10 9"><path d="M5 8.5L1 4.5A2.2 2.2 0 0 1 5 2a2.2 2.2 0 0 1 4 2.5z" fill="#fff"/></svg></span>
      </div>
      <div class="card__body" style="padding:3px 7px">
        <h3 class="card__name" style="font-size:11px">Rome Tour</h3>
        <p class="card__meta" style="font-size:5px">8 DAYS, 7 NIGHTS TOUR</p>
        <p class="card__desc" style="font-size:5px;margin-top:2px">Guided day trip with lunch and hotel pickup included.</p>
        <div class="card__row" style="margin-top:3px"><span class="price price--green" style="font-size:17px"><sup>$</sup>873</span><span class="stars" style="font-size:7px">★★★<span>★★</span></span></div>
        <div class="btn-green" style="position:relative;height:19px;font-size:6.5px;margin-top:3px">BOOK NOW</div>
      </div>
    </article>

    <article class="card" style="left:177px;top:812px;width:127px;height:156px">
      <div class="card__img card__img--horse" style="height:86px" role="img" aria-label="Photo of a rider on a brown horse on a sandy beach">
        <span class="fav fav--pink" style="right:12px;bottom:-8px;width:19px;height:19px"><svg width="10" height="9" viewBox="0 0 10 9"><path d="M5 8.5L1 4.5A2.2 2.2 0 0 1 5 2a2.2 2.2 0 0 1 4 2.5z" fill="#fff"/></svg></span>
      </div>
      <div class="card__body" style="padding:3px 7px">
        <h3 class="card__name" style="font-size:11px">Rome Tour</h3>
        <p class="card__meta" style="font-size:5px">8 DAYS, 7 NIGHTS TOUR</p>
        <p class="card__desc" style="font-size:5px;margin-top:2px">Guided day trip with lunch and hotel pickup included.</p>
        <div class="card__row" style="margin-top:3px"><span class="price" style="font-size:15px"><sup>$</sup>873</span><span class="stars" style="font-size:7px">★★★<span>★★</span></span></div>
      </div>
    </article>

    <article class="card" style="left:313px;top:812px;width:127px;height:156px">
      <div class="card__img card__img--zip" style="height:86px" role="img" aria-label="Photo of a person on a zip line in a green forest">
        <span class="fav fav--pink" style="right:12px;bottom:-8px;width:19px;height:19px"><svg width="10" height="9" viewBox="0 0 10 9"><path d="M5 8.5L1 4.5A2.2 2.2 0 0 1 5 2a2.2 2.2 0 0 1 4 2.5z" fill="#fff"/></svg></span>
      </div>
      <div class="card__body" style="padding:3px 7px">
        <h3 class="card__name" style="font-size:11px">Rome Tour</h3>
        <p class="card__meta" style="font-size:5px">8 DAYS, 7 NIGHTS TOUR</p>
        <p class="card__desc" style="font-size:5px;margin-top:2px">Guided day trip with lunch and hotel pickup included.</p>
        <div class="card__row" style="margin-top:3px"><span class="price" style="font-size:15px"><sup>$</sup>873</span><span class="stars" style="font-size:7px">★★★<span>★★</span></span></div>
      </div>
    </article>

    <article class="card" style="left:449px;top:812px;width:128px;height:156px">
      <div class="card__img card__img--bike" style="height:86px" role="img" aria-label="Photo of a mountain biker on a grassy trail">
        <span class="fav fav--pink" style="right:12px;bottom:-8px;width:19px;height:19px"><svg width="10" height="9" viewBox="0 0 10 9"><path d="M5 8.5L1 4.5A2.2 2.2 0 0 1 5 2a2.2 2.2 0 0 1 4 2.5z" fill="#fff"/></svg></span>
      </div>
      <div class="card__body" style="padding:3px 7px">
        <h3 class="card__name" style="font-size:11px">Rome Tour</h3>
        <p class="card__meta" style="font-size:5px">8 DAYS, 7 NIGHTS TOUR</p>
        <p class="card__desc" style="font-size:5px;margin-top:2px">Guided day trip with lunch and hotel pickup included.</p>
        <div class="card__row" style="margin-top:3px"><span class="price" style="font-size:15px"><sup>$</sup>873</span><span class="stars" style="font-size:7px">★★★<span>★★</span></span></div>
      </div>
    </article>
  </section>

  <!-- ===== Full-length homepage ===== -->
  <section class="screen screen--compact">
    <header class="hero" style="height:183px">
      <div class="hero__photo" role="img" aria-label="Photo of two smiling kayakers with red paddles on clear turquoise sea"></div>
      <div class="logo" style="left:98px;top:9px;font-size:11px"><span class="logo__dot" style="width:4px;height:4px"></span>uTrundle</div>
      <svg class="nav-icons" style="left:330px;top:7px" width="110" height="11" viewBox="0 0 160 16" fill="none" stroke="#fff" stroke-width="1.8">
        <path d="M8 14 L2 8 A3.5 3.5 0 0 1 8 4 A3.5 3.5 0 0 1 14 8 Z" fill="#fff"/>
        <path d="M30 3h3l2 8h8l2-6H34"/>
        <circle cx="66" cy="8" r="6.5"/><path d="M59.5 8h13"/>
        <circle cx="97" cy="8" r="6.5"/>
        <circle cx="128" cy="8" r="6.5" fill="#fff"/>
        <circle cx="153" cy="5" r="3" fill="#fff"/><path d="M147 15a6 5 0 0 1 12 0Z" fill="#fff"/>
      </svg>
      <div class="signup" style="left:442px;top:7px;width:24px;height:9px;font-size:4.5px;line-height:9px">Sign Up</div>
      <h1 class="hero__title" style="top:80px;font-size:23px;left:-2px">BOOK ACTIVITIES</h1>
      <p class="hero__sub" style="top:104px;font-size:13px;left:-2px">Your Adventure Starts Here!</p>
      <div class="search" style="left:162px;top:143px;width:196px;height:24px;padding:3px 4px;gap:5px">
        <div class="search__field" style="width:92px;font-size:6px;padding-left:4px">Where to, my friend?</div>
        <div class="search__field" style="width:92px;font-size:6px;padding-left:4px">What would you like to do?</div>
      </div>
      <div class="search__go" style="left:359px;top:142px;width:49px;height:25px;font-size:8.5px">LET'S GO!</div>
    </header>

    <p class="intro__kicker" style="top:193px;font-size:6.3px">Experience the islands with uTrundle</p>
    <p class="intro__text" style="left:142px;top:204px;width:284px;font-size:5.6px">Whether you're looking for sun and sand, a hedonistic weekend or consider yourself to be something of a culture vulture, our aim is to provide all the information you need on our favourite islands.</p>
    <div class="rule" style="left:125px;top:232px;width:315px"></div>

    <h2 class="section-title" style="top:242px;font-size:6.5px">Explore Our Top Destinations</h2>
    <svg class="abs" style="left:243px;top:252px" width="70" height="11" viewBox="0 0 100 16" fill="none" stroke-width="1.4">
      <rect x="2" y="3" width="12" height="10" rx="1" stroke="#f28a14"/>
      <path d="M93 14s-5-5-5-8a5 5 0 0 1 10 0c0 3-5 8-5 8z" stroke="#444"/>
    </svg>
    <div class="tile tile--mono" style="left:115px;top:269px;width:98px;height:98px;font-size:7.5px" role="img" aria-label="Black and white photo of a Balearic coastline">Balearic</div>
    <div class="tile tile--sea" style="left:229px;top:269px;width:97px;height:98px;font-size:7.5px" role="img" aria-label="Black and white photo of a Canary Islands beach">Canary Islands</div>
    <div class="tile tile--night" style="left:342px;top:269px;width:98px;height:98px;font-size:7.5px" role="img" aria-label="Black and white photo of Ibiza town at night">Ibiza</div>
    <div class="tile tile--feature" style="left:115px;top:380px;width:211px;height:97px;font-size:7.5px;flex-direction:column" role="img" aria-label="Colour photo of a Madeira coastal village at sunset">
      <svg width="12" height="10" viewBox="0 0 18 14" fill="none" stroke="#fff" stroke-width="1.6"><path d="M1 13c1-5 5-8 11-8V1l5 5-5 5V8c-5 0-8 1-11 5z"/></svg>
      <span style="margin-top:4px">Madeira</span>
    </div>
    <div class="select" style="left:150px;top:460px;width:62px;height:12px;font-size:4px">ACTIVITIES&nbsp;&nbsp;&nbsp;&nbsp;▾</div>
    <div class="btn-green" style="left:229px;top:460px;width:62px;height:12px;font-size:4px">BOOK NOW</div>
    <div class="tile tile--sea" style="left:342px;top:380px;width:98px;height:97px;font-size:7.5px" role="img" aria-label="Black and white photo of a Mallorca harbour">Mallorca</div>
    <div class="btn-blue" style="left:251px;top:483px;width:53px;height:14px;font-size:4.5px">Show more destinations</div>

    <div class="band" style="top:510px;height:182px"></div>
    <h2 class="section-title" style="top:514px;font-size:7.5px">Explore Our Top Activities</h2>
    <div class="finder" style="left:263px;top:526px;font-size:4.5px">
      <svg width="6" height="6" viewBox="0 0 9 9" fill="none" stroke="#111" stroke-width="1.4"><circle cx="3.6" cy="3.6" r="2.7"/><path d="M5.6 5.6L8.4 8.4"/></svg>Type to search ...
    </div>
    <div class="tabs" style="left:204px;top:537px;width:158px;font-size:4.5px"><span class="is-active">RECOMMENDED</span><span>DESTINATION</span><span>MOST POPULAR</span></div>

    <div class="arrow" style="left:77px;top:607px;width:10px;height:10px;font-size:6px">←</div>
    <div class="arrow" style="left:477px;top:607px;width:10px;height:10px;font-size:6px">→</div>

    <article class="card card--featured" style="left:98px;top:551px;width:88px;height:124px">
      <div class="card__img card__img--snorkel" style="height:59px" role="img" aria-label="Photo of snorkellers in clear blue water">
        <span class="fav fav--green" style="right:8px;bottom:-6px;width:13px;height:13px"></span>
      </div>
      <div class="card__body" style="padding:2px 5px">
        <h3 class="card__name" style="font-size:7.5px">Rome Tour</h3>
        <p class="card__meta" style="font-size:3.5px">8 DAYS, 7 NIGHTS TOUR</p>
        <p class="card__desc" style="font-size:3.5px;margin-top:1px">Guided day trip with lunch and hotel pickup included.</p>
        <div class="card__row" style="margin-top:2px"><span class="price price--green" style="font-size:12px"><sup>$</sup>873</span><span class="stars" style="font-size:5px">★★★<span>★★</span></span></div>
        <div class="btn-green" style="position:relative;height:13px;font-size:4.5px;margin-top:2px">BOOK NOW</div>
      </div>
    </article>

    <article class="card" style="left:192px;top:559px;width:88px;height:108px">
      <div class="card__img card__img--horse" style="height:59px" role="img" aria-label="Photo of a rider on a horse on a beach">
        <span class="fav fav--pink" style="right:8px;bottom:-6px;width:13px;height:13px"></span>
      </div>
      <div class="card__body" style="padding:2px 5px">
        <h3 class="card__name" style="font-size:7.5px">Rome Tour</h3>
        <p class="card__meta" style="font-size:3.5px">8 DAYS, 7 NIGHTS TOUR</p>
        <p class="card__desc" style="font-size:3.5px;margin-top:1px">Guided day trip with lunch and hotel pickup included.</p>
        <div class="card__row" style="margin-top:2px"><span class="price" style="font-size:11px"><sup>$</sup>873</span><span class="stars" style="font-size:5px">★★★<span>★★</span></span></div>
      </div>
    </article>

    <article class="card" style="left:285px;top:559px;width:88px;height:108px">
      <div class="card__img card__img--zip" style="height:59px" role="img" aria-label="Photo of a person on a zip line in a forest">
        <span class="fav fav--pink" style="right:8px;bottom:-6px;width:13px;height:13px"></span>
      </div>
      <div class="card__body" style="padding:2px 5px">
        <h3 class="card__name" style="font-size:7.5px">Rome Tour</h3>
        <p class="card__meta" style="font-size:3.5px">8 DAYS, 7 NIGHTS TOUR</p>
        <p class="card__desc" style="font-size:3.5px;margin-top:1px">Guided day trip with lunch and hotel pickup included.</p>
        <div class="card__row" style="margin-top:2px"><span class="price" style="font-size:11px"><sup>$</sup>873</span><span class="stars" style="font-size:5px">★★★<span>★★</span></span></div>
      </div>
    </article>

    <article class="card" style="left:379px;top:559px;width:89px;height:108px">
      <div class="card__img card__img--bike" style="height:59px" role="img" aria-label="Photo of a mountain biker on a trail">
        <span class="fav fav--pink" style="right:8px;bottom:-6px;width:13px;height:13px"></span>
      </div>
      <div class="card__body" style="padding:2px 5px">
        <h3 class="card__name" style="font-size:7.5px">Rome Tour</h3>
        <p class="card__meta" style="font-size:3.5px">8 DAYS, 7 NIGHTS TOUR</p>
        <p class="card__desc" style="font-size:3.5px;margin-top:1px">Guided day trip with lunch and hotel pickup included.</p>
        <div class="card__row" style="margin-top:2px"><span class="price" style="font-size:11px"><sup>$</sup>873</span><span class="stars" style="font-size:5px">★★★<span>★★</span></span></div>
      </div>
    </article>

    <div class="rule" style="left:98px;top:715px;width:145px"></div>
    <h2 class="islands__title" style="left:248px;top:709px">Explore <b>by Island</b></h2>
    <div class="rule" style="left:322px;top:715px;width:145px"></div>
    <div class="islands__col" style="left:138px;top:727px"><h4>CANARY ISLANDS</h4>Tenerife<br>Gran Canaria<br>Fuerteventura<br>La Palma<br>Lanzarote<br>La Gomera<br>El Hierro</div>
    <div class="islands__col" style="left:208px;top:727px"><h4>MADEIRA ARCHIPELAGO</h4>Madeira<br>Porto Santo</div>
    <div class="islands__col" style="left:295px;top:727px"><h4>BALEARIC ISLANDS</h4>Ibiza<br>Formentera<br>Mallorca<br>Menorca</div>
    <div class="islands__col" style="left:368px;top:727px"><h4>MALTESE ARCHIPELAGO</h4>Malta</div>

    <div class="newsletter" style="top:835px;height:48px">
      <p class="newsletter__text" style="left:142px;top:14px;width:140px">Discover exciting travel tips, city guides, and top deals every week on uTrundle.</p>
      <div class="newsletter__input" style="left:285px;top:17px;width:80px;height:13px">ENTER YOUR EMAIL</div>
      <div class="btn-blue" style="left:370px;top:17px;width:52px;height:13px;font-size:5px;font-weight:400">SUBSCRIBE</div>
    </div>

    <footer class="footer" style="top:883px;height:117px">
      <div class="logo" style="left:98px;top:14px;font-size:11px;color:var(--ink)"><span class="logo__dot" style="width:4px;height:4px"></span>uTrundle</div>
      <p class="footer__col" style="left:98px;top:28px;line-height:7px">© 2015, uTrundle, LLC.<br>All Rights Reserved.</p>
      <div class="footer__col" style="left:176px;top:16px"><h5>COMPANY</h5>About uTrundle.net<br>Corporate info<br>Blog<br>Careers</div>
      <div class="footer__col" style="left:243px;top:16px"><h5>SUPPORT</h5>Contact us<br>FAQs<br>Legal<br>Privacy Policy<br>Legal</div>
      <div class="footer__col" style="left:302px;top:16px"><h5>PARTNERSHIPS</h5>Supplier sign-up<br>Affiliate Programs</div>
      <div class="footer__col" style="left:375px;top:16px"><h5>LOG-INS</h5>Customers<br>Suppliers<br>Affiliates</div>
      <div class="footer__col" style="left:441px;top:16px"><h5>SOCIAL</h5><div class="social"><i></i><i></i><i></i><i></i></div></div>
    </footer>
  </section>

</div>
</body>
</html>
```